Trade Show Poster/Booth Backdrop for Rugged Technology Business

I need a graphic design for an 8' x 6' poster to hang on back wall of my event booth. Design must be consistent with my company's colors, logo, and current branding as shown on website, Facebook, and Social (links provided). You can propose other elements, but there are certain core images and text elements that must be incorporated. Print specifications also provided. File must be delivered on time and upload-ready.

Font styles to use
Sans Serif

Colors
33a6d7
0355a3
33b8a4
00a990
9bcb3b
abd036
cadf82
85cae6
86cfc6

Requirements
Nice to have
• Regarding color, I'm okay with designs using the orange version of the Vorlin logo.
• Regarding the images I provided as potential background layers, I especially like the ones with rocky island profiles and exposed cliff faces. In addition to being a nice match color wise, they are subtle suggestions of ruggedness and working with technology that can handle extreme environments (which is a big part of the messaging focus).
Should not have
• Vibrant coloration is very much desired and OK, but please avoid a blend that goes to either extreme. For instance, too much dark blue makes it look like every other tech company ever. Too much warm, light green (other than for contrast elements) makes it look too tropical and casual.

```html
<!DOCTYPE html>
<html lang="en">
<head>
<meta charset="utf-8">
<title>Talvaro Ridgeworks – Booth Backdrop</title>
<link rel="stylesheet" href="https://fonts.googleapis.com/css2?family=Montserrat:wght@300;400;600;700;800&display=swap">
<style>
  :root {
    --blue-deep: #0355a3;
    --blue-sky: #33a6d7;
    --blue-pale: #85cae6;
    --teal: #00a990;
    --teal-soft: #33b8a4;
    --green: #3aa54a;
    --lime: #9bcb3b;
    --lime-pale: #cadf82;
    --grey: #8a8d90;
    --ink: #2a2d33;
    --white: #ffffff;
  }
  html, body {
    margin: 0;
    padding: 0;
    width: 1200px;
    height: 960px;
    overflow: hidden;
    background: var(--white);
  }
  .backdrop {
    display: block;
    width: 1200px;
    height: 960px;
    font-family: "Montserrat", sans-serif;
  }
  .brand-name { font-weight: 600; fill: var(--green); letter-spacing: 6px; }
  .headline-light { font-weight: 300; fill: var(--white); }
  .headline-bold { font-weight: 800; fill: var(--white); }
  .service-label { font-weight: 700; fill: var(--white); font-size: 25px; }
  .contact-label { font-weight: 700; fill: var(--ink); font-size: 24px; }
  .contact-text { font-weight: 400; fill: var(--ink); font-size: 22px; }
  .partner-name { font-weight: 700; fill: var(--grey); font-size: 84px; }
  .icon-fill { fill: var(--teal); }
</style>
</head>
<body>
<svg class="backdrop" viewBox="0 0 1200 960" xmlns="http://www.w3.org/2000/svg">
  <defs>
    <linearGradient id="sky-tone" x1="0" y1="0" x2="0" y2="1">
      <stop offset="0" stop-color="#ffffff"/>
      <stop offset="1" stop-color="#eef1f3"/>
    </linearGradient>
    <linearGradient id="band-tone" x1="0" y1="0" x2="1" y2="0">
      <stop offset="0" stop-color="#0d58a4"/>
      <stop offset="0.5" stop-color="#1a7f9c"/>
      <stop offset="1" stop-color="#3aa54a"/>
    </linearGradient>
    <linearGradient id="band-shade" x1="0" y1="0" x2="0" y2="1">
      <stop offset="0" stop-color="#000" stop-opacity="0"/>
      <stop offset="0.55" stop-color="#0b3f3a" stop-opacity="0.18"/>
      <stop offset="1" stop-color="#000" stop-opacity="0.05"/>
    </linearGradient>
    <linearGradient id="ring-tone" x1="0" y1="0" x2="1" y2="1">
      <stop offset="0" stop-color="#33a6d7"/>
      <stop offset="1" stop-color="#9bcb3b"/>
    </linearGradient>
    <linearGradient id="lime-edge" x1="0" y1="0" x2="1" y2="0">
      <stop offset="0" stop-color="#cadf82" stop-opacity="0"/>
      <stop offset="0.5" stop-color="#abd036"/>
      <stop offset="1" stop-color="#9bcb3b"/>
    </linearGradient>
  </defs>

  <!-- sky area -->
  <rect class="sky-scene" x="0" y="0" width="1200" height="330" fill="url(#sky-tone)" role="img" aria-label="Soft cloudy sky above a rocky island coastline"/>

  <!-- main colour band with island scenery -->
  <path class="hero-band" d="M0,118 C160,175 320,270 560,282 C800,292 1000,210 1200,118 L1200,722 C900,740 600,790 0,792 Z" fill="url(#band-tone)" role="img" aria-label="Rocky islands and forested cliffs over calm water, tinted blue to green"/>
  <path d="M0,118 C160,175 320,270 560,282 C800,292 1000,210 1200,118 L1200,722 C900,740 600,790 0,792 Z" fill="url(#band-shade)"/>

  <!-- white top wave with lime edge -->
  <path class="top-wave" d="M0,0 H1200 V118 C1000,210 800,292 560,282 C320,270 160,175 0,118 Z" fill="url(#sky-tone)"/>
  <path class="top-wave-edge" d="M300,230 C400,270 470,284 560,288 C800,298 1000,214 1200,120" fill="none" stroke="url(#lime-edge)" stroke-width="12"/>

  <!-- bottom bands -->
  <path class="bottom-green" d="M0,792 C600,790 900,740 1200,722 L1200,752 C900,772 600,828 0,830 Z" fill="var(--green)"/>
  <path class="bottom-grey" d="M0,830 C600,828 900,772 1200,752 L1200,770 C900,792 600,846 0,848 Z" fill="#c9cbcd"/>
  <path class="bottom-white" d="M0,848 C600,846 900,792 1200,770 L1200,960 L0,960 Z" fill="var(--white)"/>

  <!-- brand -->
  <g class="brand">
    <circle cx="362" cy="140" r="62" fill="var(--blue-sky)"/>
    <text class="brand-name" x="458" y="162" font-size="64">TALVARO</text>
    <text class="brand-name" x="800" y="212" font-size="32" text-anchor="end" letter-spacing="3">Ridgeworks</text>
  </g>

  <!-- headline -->
  <text class="headline-light" x="600" y="368" font-size="56" text-anchor="middle">FULLY RUGGED &amp; BUSINESS CLASS</text>
  <text class="headline-bold" x="600" y="436" font-size="68" text-anchor="middle">TECHNOLOGY SOLUTIONS</text>

  <!-- services -->
  <g class="services">
    <!-- mobility -->
    <g transform="translate(180,551)">
      <circle r="67" fill="url(#ring-tone)"/>
      <circle r="57" fill="var(--white)"/>
      <rect x="-22" y="-32" width="34" height="60" rx="6" class="icon-fill"/>
      <rect x="-16" y="-22" width="22" height="38" fill="var(--white)"/>
      <circle cx="-5" cy="22" r="3" fill="var(--white)"/>
      <path d="M2,-8 H16 V-18 L32,0 L16,18 V8 H2 Z" class="icon-fill" stroke="var(--white)" stroke-width="3"/>
      <text class="service-label" y="110" text-anchor="middle">Mobility</text>
    </g>
    <!-- computing -->
    <g transform="translate(348,551)">
      <circle r="67" fill="url(#ring-tone)"/>
      <circle r="57" fill="var(--white)"/>
      <path d="M-20,-14 a12,12 0 0 1 4,-22 a16,16 0 0 1 30,2 a11,11 0 0 1 6,20 Z" class="icon-fill"/>
      <path d="M0,-14 V4 M-28,4 H28 M-28,4 V12 M0,4 V12 M28,4 V12" stroke="var(--teal)" stroke-width="3" fill="none"/>
      <rect x="-40" y="12" width="22" height="15" fill="none" stroke="var(--teal)" stroke-width="3"/>
      <rect x="-7" y="12" width="14" height="18" fill="none" stroke="var(--teal)" stroke-width="3"/>
      <rect x="18" y="12" width="22" height="15" fill="none" stroke="var(--teal)" stroke-width="3"/>
      <text class="service-label" y="110" text-anchor="middle">Computing</text>
    </g>
    <!-- mounting -->
    <g transform="translate(516,551)">
      <circle r="67" fill="url(#ring-tone)"/>
      <circle r="57" fill="var(--white)"/>
      <path d="M-38,28 L-14,-12 L-4,2 L12,-34 L40,28 Z" class="icon-fill"/>
      <path d="M6,-20 L12,-34 L20,-16 L14,-20 Z" fill="var(--white)"/>
      <text class="service-label" y="110" text-anchor="middle">Mounting</text>
    </g>
    <!-- printing -->
    <g transform="translate(683,551)">
      <circle r="67" fill="url(#ring-tone)"/>
      <circle r="57" fill="var(--white)"/>
      <rect x="-18" y="-36" width="32" height="22" class="icon-fill"/>
      <rect x="-34" y="-12" width="68" height="30" rx="4" class="icon-fill"/>
      <rect x="-20" y="8" width="40" height="24" fill="var(--white)" stroke="var(--teal)" stroke-width="4"/>
      <path d="M-12,16 H12 M-12,24 H12" stroke="var(--teal)" stroke-width="3"/>
      <text class="service-label" y="110" text-anchor="middle">Printing</text>
    </g>
    <!-- imaging -->
    <g transform="translate(852,551)">
      <circle r="67" fill="url(#ring-tone)"/>
      <circle r="57" fill="var(--white)"/>
      <circle cy="-8" r="14" fill="none" stroke="var(--teal)" stroke-width="4"/>
      <rect x="-6" y="6" width="12" height="12" class="icon-fill"/>
      <path d="M0,-34 V-40 M-24,-8 H-32 M24,-8 H32 M-17,-25 L-23,-31 M17,-25 L23,-31" stroke="var(--teal)" stroke-width="4"/>
      <text class="service-label" y="110" text-anchor="middle">Imaging</text>
    </g>
    <!-- storage -->
    <g transform="translate(1019,551)">
      <circle r="67" fill="url(#ring-tone)"/>
      <circle r="57" fill="var(--white)"/>
      <ellipse cy="-24" rx="26" ry="9" class="icon-fill"/>
      <path d="M-26,-16 a26,9 0 0 0 52,0 V-4 a26,9 0 0 1 -52,0 Z" class="icon-fill"/>
      <path d="M-26,4 a26,9 0 0 0 52,0 V16 a26,9 0 0 1 -52,0 Z" class="icon-fill"/>
      <path d="M-26,24 a26,9 0 0 0 52,0 V32 a26,9 0 0 1 -52,0 Z" class="icon-fill"/>
      <text class="service-label" y="110" text-anchor="middle">Storage</text>
    </g>
  </g>

  <!-- contact -->
  <g class="contact">
    <circle cx="86" cy="888" r="13" fill="var(--blue-sky)"/>
    <text x="112" y="896"><tspan class="contact-label">Social: </tspan><tspan class="contact-text">@TalvaroforIT</tspan></text>
    <text class="contact-text" x="410" y="878">www.talvaroridgeworks.net</text>
  </g>

  <!-- partner -->
  <text class="partner-name" x="1150" y="900" text-anchor="end">Vorlin</text>
</svg>
</body>
</html>
```